Corvale Homes

To produce a business card design for our newly established house building and development company, We have had a logo design done please see attached, our slogan is "building your home sweet home"
Contact Information for Business Card
Adress on card needs to Read - 58 Elmsworth Lane, Kettering, Northamptonshire NN16 4QT. Director name Dean Vascotti
Requirements
Must have
- Web adress is www.corvale-homes.co.uk
- Email address is info@corvale-homes.co.uk
- phone number 07700 900417

```html
<!DOCTYPE html>
<html lang="en">
<head>
<meta charset="utf-8">
<title>Corvale Homes – Business Card</title>
<link href="https://fonts.googleapis.com/css2?family=Montserrat:wght@800&family=Open+Sans:wght@400;600&display=swap" rel="stylesheet">
<style>
  :root {
    --bg: #e9eef2;
    --card-dark: #161819;
    --card-mid: #2f3335;
    --green: #8ee01f;
    --green-deep: #6fc21a;
    --white: #ffffff;
    --grey: #c9cdd0;
  }
  * { margin: 0; padding: 0; box-sizing: border-box; }
  html, body {
    width: 1200px; height: 1200px; overflow: hidden;
    background: var(--bg);
    font-family: "Open Sans", Arial, sans-serif;
  }
  .sheet {
    width: 1200px; height: 1200px;
    display: flex; flex-direction: column; align-items: center; justify-content: center;
    gap: 50px;
  }
  .card {
    position: relative;
    width: 900px; height: 514px;
    border-radius: 6px; overflow: hidden;
    box-shadow: 0 10px 30px rgba(0,0,0,.18);
  }
  .card svg.card-art { position: absolute; inset: 0; width: 100%; height: 100%; }
  .brand-name {
    position: absolute;
    font-family: "Montserrat", Arial, sans-serif; font-weight: 800;
    color: var(--green); letter-spacing: 2px; text-transform: uppercase;
    white-space: nowrap; transform: translate(-50%, -50%);
  }
  .card-front .brand-name { left: 50%; top: 64%; font-size: 48px; }
  .card-back .brand-name { left: 215px; top: 52%; font-size: 32px; }

  .contact-panel {
    position: absolute; left: 585px; top: 80px; width: 300px; color: var(--white);
  }
  .person-name {
    font-family: "Montserrat", Arial, sans-serif; font-weight: 800;
    font-size: 30px; letter-spacing: 1px; text-transform: uppercase;
  }
  .person-role {
    display: flex; align-items: center; gap: 12px; margin-top: 4px; margin-left: 40px;
    font-size: 14px; letter-spacing: 1px; color: var(--grey);
  }
  .person-role::before, .person-role::after {
    content: ""; width: 28px; height: 3px; background: var(--green);
  }
  .contact-list { list-style: none; margin-top: 46px; display: flex; flex-direction: column; gap: 26px; }
  .contact-item { display: flex; align-items: center; gap: 16px; font-size: 16px; line-height: 1.35; }
  .contact-icon {
    flex: none; width: 38px; height: 38px; border-radius: 50%;
    background: var(--green); display: flex; align-items: center; justify-content: center;
  }
  .contact-icon svg { width: 20px; height: 20px; }
  .contact-phone { font-weight: 600; font-size: 18px; letter-spacing: 1px; }
</style>
</head>
<body>
<main class="sheet">

  <section class="card card-front" aria-label="Business card front">
    <svg class="card-art" viewBox="0 0 900 514" preserveAspectRatio="none">
      <defs>
        <linearGradient id="frontBg" x1="0" y1="0" x2="0" y2="1">
          <stop offset="0" stop-color="#33383a"/>
          <stop offset="1" stop-color="#121414"/>
        </linearGradient>
      </defs>
      <rect width="900" height="514" fill="url(#frontBg)"/>
      <path class="wave-band" d="M0,300 C180,180 380,150 560,130 C700,115 820,90 900,58 L900,92 C820,118 700,140 560,152 C380,170 200,215 0,334 Z" fill="var(--green)"/>
      <path class="wave-shade" d="M0,334 C200,215 380,170 560,152 C700,140 820,118 900,92 L900,100 C820,126 700,146 560,158 C380,176 200,222 0,342 Z" fill="var(--green-deep)"/>
    </svg>
    <div class="brand-name">Corvale Homes</div>
  </section>

  <section class="card card-back" aria-label="Business card back">
    <svg class="card-art" viewBox="0 0 900 514" preserveAspectRatio="none">
      <defs>
        <linearGradient id="backBg" x1="0" y1="0" x2="0" y2="1">
          <stop offset="0" stop-color="#34393b"/>
          <stop offset="1" stop-color="#1b1e1f"/>
        </linearGradient>
        <linearGradient id="cityTone" x1="0" y1="0" x2="1" y2="1">
          <stop offset="0" stop-color="#2a2d2e"/>
          <stop offset="1" stop-color="#101212"/>
        </linearGradient>
      </defs>
      <rect width="900" height="514" fill="url(#backBg)"/>
      <path class="green-curve" d="M270,0 L360,0 C470,120 520,230 480,330 C455,400 470,470 520,514 L470,514 C420,470 410,400 430,330 C460,230 400,120 270,0 Z" fill="var(--green)"/>
      <path class="green-curve-inner" d="M270,0 L322,0 C430,120 480,230 445,330 C420,400 430,470 480,514 L470,514 C420,470 410,400 430,330 C460,230 400,120 270,0 Z" fill="var(--green-deep)"/>
      <path role="img" aria-label="Faint aerial photograph of a city skyline" d="M0,0 L270,0 C400,120 460,230 430,330 C410,400 420,470 470,514 L0,514 Z" fill="url(#cityTone)"/>
    </svg>
    <div class="brand-name">Corvale Homes</div>

    <div class="contact-panel">
      <div class="person-name">Dean Vascotti</div>
      <div class="person-role">DIRECTOR</div>
      <ul class="contact-list">
        <li class="contact-item">
          <span class="contact-icon"><svg viewBox="0 0 24 24"><path d="M6.6 10.8c1.4 2.8 3.8 5.1 6.6 6.6l2.2-2.2c.3-.3.7-.4 1-.2 1.1.4 2.3.6 3.6.6.6 0 1 .4 1 1V20c0 .6-.4 1-1 1C10.6 21 3 13.4 3 4c0-.6.4-1 1-1h3.5c.6 0 1 .4 1 1 0 1.3.2 2.5.6 3.6.1.3 0 .7-.2 1z" fill="#fff"/></svg></span>
          <span class="contact-phone">07700 900417</span>
        </li>
        <li class="contact-item">
          <span class="contact-icon"><svg viewBox="0 0 24 24" fill="none" stroke="#fff" stroke-width="1.8"><circle cx="12" cy="12" r="9"/><ellipse cx="12" cy="12" rx="4" ry="9"/><path d="M3 12h18M5 7h14M5 17h14"/></svg></span>
          <span>www.corvale-homes.co.uk<br>info@corvale-homes.co.uk</span>
        </li>
        <li class="contact-item">
          <span class="contact-icon"><svg viewBox="0 0 24 24" fill="none" stroke="#fff" stroke-width="1.8"><path d="M12 21s-6-6.2-6-11a6 6 0 0 1 12 0c0 4.8-6 11-6 11z"/><circle cx="12" cy="10" r="2.2"/></svg></span>
          <span>58 Elmsworth Lane, Kettering,<br>Northamptonshire NN16 4QT</span>
        </li>
      </ul>
    </div>
  </section>

</main>
</body>
</html>
```